Professional Website

We are looking for a new website for our Staffing Company. Attached is a document with all the details and pages needed along with some examples of others websites.

We want a professional Look and feel around the same color theme as the attached Vivid Vision.

We currently host our site on SiteKarn.io. If the winning designer can also add to SiteKarn, that is a plus.

```html
<!DOCTYPE html>
<html lang="en">
<head>
<meta charset="utf-8">
<title>CrewLine Clerical &amp; Industrial</title>
<link href="https://fonts.googleapis.com/css2?family=Raleway:wght@300;400;500;600;700;800&display=swap" rel="stylesheet">
<style>
:root{
  --blue:#2540b8;
  --blue-deep:#0f1e8a;
  --dark:#232323;
  --ink:#2b2b2b;
  --white:#ffffff;
  --hero-a:#3a4768;
  --hero-b:#6b7289;
  --photo-a:#f1dcc0;
  --photo-b:#6d7a88;
}
*{margin:0;padding:0;box-sizing:border-box}
html,body{width:1200px;height:2692px;overflow:hidden}
body{position:relative;background:var(--white);font-family:'Raleway',sans-serif;color:var(--ink)}
.hero{position:absolute;left:0;top:0;width:1200px;height:830px;
  background:radial-gradient(ellipse at 60% 30%,var(--hero-b),var(--hero-a) 70%,#262d45)}
.hero-cut{position:absolute;left:0;top:560px}
.header{position:absolute;left:89px;top:22px;right:89px;height:60px;display:flex;align-items:center}
.brand{display:flex;flex-direction:column;color:var(--white)}
.brand-name{font-weight:800;font-size:38px;letter-spacing:-1px;line-height:1}
.brand-sub{font-weight:600;font-size:9px;letter-spacing:1.5px;margin-top:2px}
.nav{margin-left:auto;display:flex;gap:31px;margin-right:45px}
.nav a{color:var(--white);text-decoration:none;font-weight:700;font-size:15px}
.hotline{display:flex;align-items:center;gap:10px;color:var(--white)}
.hotline .dot{width:36px;height:36px;border-radius:50%;background:var(--blue);display:flex;align-items:center;justify-content:center}
.hotline small{display:block;font-weight:700;font-size:14px}
.hotline strong{display:block;font-weight:800;font-size:18px;letter-spacing:.5px}
.hero-title{position:absolute;left:0;right:0;top:272px;text-align:center;color:var(--white);
  font-weight:800;font-size:50px;line-height:58px}
.scroll-cue{position:absolute;left:589px;top:613px}
.cards{position:absolute;left:176px;top:864px;display:flex;gap:15px}
.card{width:423px;height:329px;display:flex;flex-direction:column;align-items:center;justify-content:center;color:var(--white)}
.card--seek{background:var(--blue)}
.card--hire{background:var(--dark)}
.card h2{font-weight:700;font-size:35px;margin-top:6px}
.card p{font-weight:400;font-size:20px}
.intro{position:absolute;left:176px;top:1283px;width:862px}
.intro h2{font-weight:700;font-size:35px;line-height:45px;color:var(--ink)}
.intro p{font-size:15px;line-height:23px;margin-top:18px}
.intro p+p{margin-top:0}
.photo{position:absolute;left:176px;top:1610px;width:862px;height:491px;
  background:linear-gradient(120deg,var(--photo-a),#c9a58a 40%,var(--photo-b))}
.accent-bar{position:absolute;left:234px;top:1514px;width:7px;height:206px;background:var(--blue)}
.footer-shape{position:absolute;left:0;top:2180px}
.footer{position:absolute;left:0;top:2426px;width:1200px;height:266px;background:var(--dark);color:var(--white)}
.footer .brand{position:absolute;left:162px;top:47px}
.footer .brand-name{font-size:46px}
.footer .brand-sub{font-size:11px}
.areas{position:absolute;left:536px;top:47px}
.areas h3,.f-hot h3{font-weight:700;font-size:23px;margin-left:3px}
.areas li{list-style:none;font-size:15px;line-height:28px;margin-top:2px}
.f-hot{position:absolute;left:826px;top:47px}
.f-hot strong{display:block;font-weight:800;font-size:30px;color:var(--blue);letter-spacing:1px}
.rule{position:absolute;left:89px;right:89px;top:219px;height:1px;background:#555}
.copy{position:absolute;left:0;right:0;top:236px;text-align:center;font-size:15px}
.to-top{position:absolute;left:1112px;top:199px;width:40px;height:40px;border-radius:50%;background:var(--blue);display:flex;align-items:center;justify-content:center}
</style>
</head>
<body>
<section class="hero" role="img" aria-label="Blurred photo of commuters walking through a city at dusk">
  <header class="header">
    <div class="brand"><span class="brand-name">CrewLine</span><span class="brand-sub">CLERICAL &amp; INDUSTRIAL</span></div>
    <nav class="nav"><a href="#">Employee Login</a><a href="#">Pay Card Login</a><a href="#">Partner Bank Login</a></nav>
    <div class="hotline">
      <span class="dot"><svg width="18" height="18" viewBox="0 0 24 24"><path fill="#fff" d="M6.6 10.8a15 15 0 006.6 6.6l2.2-2.2a1 1 0 011-.25 11 11 0 003.6.6 1 1 0 011 1V20a1 1 0 01-1 1A17 17 0 013 4a1 1 0 011-1h3.5a1 1 0 011 1 11 11 0 00.6 3.6 1 1 0 01-.25 1z"/></svg></span>
      <span><small>Hotline</small><strong>708-555-0142</strong></span>
    </div>
  </header>
  <h1 class="hero-title">We help people with our<br>best services, Not only at work,<br>but in life.</h1>
  <svg class="scroll-cue" width="22" height="34" viewBox="0 0 22 34"><rect x="1.5" y="1.5" width="19" height="31" rx="9.5" fill="none" stroke="#fff" stroke-width="2"/><line x1="11" y1="8" x2="11" y2="14" stroke="#fff" stroke-width="2"/></svg>
  <svg class="hero-cut" width="1200" height="270" viewBox="0 0 1200 270"><polygon points="646,125 1200,10 1200,270" fill="var(--blue-deep)"/><polygon points="0,262 646,125 1200,266 1200,270 0,270" fill="#fff"/></svg>
</section>

<div class="cards">
  <a class="card card--seek">
    <svg width="128" height="124" viewBox="0 0 128 124"><circle cx="52" cy="50" r="44" fill="none" stroke="#fff" stroke-width="6"/><circle cx="52" cy="50" r="34" fill="none" stroke="#fff" stroke-width="3"/><text x="52" y="60" text-anchor="middle" font-family="Raleway,sans-serif" font-weight="800" font-size="26" fill="#fff">JOB</text><line x1="84" y1="84" x2="116" y2="116" stroke="#fff" stroke-width="14" stroke-linecap="round"/><line x1="84" y1="84" x2="116" y2="116" stroke="var(--blue)" stroke-width="6" stroke-linecap="round"/></svg>
    <h2>I’m Looking For a Job</h2><p>job seekers</p>
  </a>
  <a class="card card--hire">
    <svg width="180" height="100" viewBox="0 0 180 100"><g fill="none" stroke="#fff" stroke-width="7"><circle cx="38" cy="22" r="16"/><path d="M4 62a34 30 0 0168 0"/><circle cx="142" cy="22" r="16"/><path d="M108 62a34 30 0 0168 0"/><circle cx="90" cy="48" r="16"/><path d="M56 96a34 30 0 0168 0"/></g></svg>
    <h2>I Need Employees</h2><p>employers</p>
  </a>
</div>

<section class="intro">
  <h2>Greatest part of our daily job is that we are constantly bringing people together.</h2>
  <p>Our Clients come to us in search of the perfect candidate and the job hunters approach us when they are in need of a job or looking for their next exciting role.</p>
  <p>Being able to work with and connect the two is incredibly satisfying. Not to mention that in today’s current job market, employers are fighting for the top talent. This makes our employees and partners grateful for the help in finding it!</p>
</section>

<div class="photo" role="img" aria-label="Photo of many raised hands giving a group high five with networking icons overlaid"></div>
<div class="accent-bar"></div>

<svg class="footer-shape" width="1200" height="250" viewBox="0 0 1200 250"><polygon points="0,246 1200,0 1200,250 0,250" fill="var(--dark)"/></svg>
<footer class="footer">
  <div class="brand"><span class="brand-name">CrewLine</span><span class="brand-sub">CLERICAL &amp; INDUSTRIAL</span></div>
  <div class="areas"><h3>Areas we service</h3><ul><li>Maple Ridge</li><li>Cedar Falls</li><li>Lakeview</li></ul></div>
  <div class="f-hot"><h3>Hotline</h3><strong>708-555-0142</strong></div>
  <div class="rule"></div>
  <a class="to-top"><svg width="10" height="8" viewBox="0 0 10 8"><path d="M1 6l4-4 4 4" fill="none" stroke="#fff" stroke-width="1.6"/></svg></a>
  <p class="copy">©Copyright 2022 | All Rights Reserved</p>
</footer>
</body>
</html>
```